Posters to advertise a jewellery design school

I would like two pieces of artwork designing for our jewellery design school in Kuala Lumpur Malaysia.
60cm by 180cm poster
100cm by 100cm poster

My personal style is ‘perfectly imperfect’ but we wold like to show that we give quality classes in a fun and artistic / creative environment

The posters must contain our logo and you can choose to use as many or as few images as you like to tell the story or even include hand drawn line images.

https://files.brambleshare.net/folders/7kQzWmR2pLxT8nYv__HbS3dFj6cNa9Ec?usp=sharing

Please include the following wording on the poster
So you want to be a jewellery designer?

Part time and full-time classes available in:
Silversmithing
Jewellery design and rendering
Stone setting
Gemmology
Enamelling
Computer aided design
60cm by 180cm poster
100cm by 100cm poster

The posters must contain our logo and you can choose to use as many or as few images as you like to tell the story.

Silversmithing
Stone setting
Gemmology
Enamelling
Computer aided design

60cm by 180cm poster
100cm by 100cm poster

Silversmithing
Stone setting
Gemmology
Enamelling
Computer aided design

```html
<!DOCTYPE html>
<html lang="en">
<head>
<meta charset="utf-8">
<title>Mara Linden jewellery – school poster</title>
<link href="https://fonts.googleapis.com/css2?family=Questrial&family=Montserrat:wght@600&family=Source+Sans+3:wght@400&display=swap" rel="stylesheet">
<style>
  :root{
    --teal:#0e7377;
    --grey:#5b5b5d;
    --ink:#ffffff;
    --stage:#000000;
    --paper:#ffffff;
    --mist:#e9edef;
  }
  html,body{margin:0;padding:0;overflow:hidden;background:var(--stage);}
  .stage{position:relative;width:1000px;height:1200px;background:var(--stage);overflow:hidden;font-family:"Questrial",sans-serif;}
  .poster{position:absolute;left:318px;top:43px;width:364px;height:1080px;
    background:radial-gradient(ellipse at 30% 20%,var(--paper) 0%,var(--mist) 60%,var(--paper) 100%);overflow:hidden;}
  .poster-art{position:absolute;left:0;top:0;width:364px;height:1080px;}
  .brand{position:absolute;left:0;top:36px;width:230px;text-align:center;color:var(--grey);font-weight:400;}
  .brand-mark{width:74px;height:74px;border-radius:50%;background:var(--grey);margin:0 auto 10px;}
  .brand-name{font-size:21px;letter-spacing:.5px;line-height:1;}
  .brand-sub{font-size:14px;letter-spacing:1px;margin-top:6px;}
  .headline{position:absolute;left:0;top:596px;width:282px;text-align:right;}
  .headline-lead{font-size:19px;color:var(--grey);line-height:22px;}
  .headline-lead .hl{background:var(--teal);color:var(--ink);padding:0 2px;}
  .headline-main{font-size:55px;color:var(--grey);line-height:50px;letter-spacing:-1px;margin-top:2px;}
  .headline-accent{font-family:"Montserrat",sans-serif;font-weight:600;font-size:35px;color:var(--teal);line-height:36px;margin-right:2px;}
  .offer{position:absolute;left:0;top:735px;width:280px;}
  .offer-line{display:block;background:var(--teal);color:var(--ink);text-align:right;font-size:18px;line-height:19px;padding-right:2px;margin-bottom:3px;}
  .courses{position:absolute;left:40px;top:792px;margin:0;padding:0;list-style:none;}
  .courses li{position:relative;padding-left:24px;font-size:18px;color:var(--grey);line-height:26.5px;}
  .courses li::before{content:"";position:absolute;left:0;top:7px;border-left:13px solid var(--teal);border-top:7px solid transparent;border-bottom:7px solid transparent;}
  .footer-band{position:absolute;left:0;bottom:0;width:364px;height:31px;background:var(--teal);}
  .size-note{position:absolute;left:0;top:1143px;width:1000px;text-align:center;color:var(--ink);font-family:"Source Sans 3",sans-serif;font-size:18px;}
</style>
</head>
<body>
<div class="stage">
  <div class="poster">
    <svg class="poster-art" viewBox="0 0 364 1080" xmlns="http://www.w3.org/2000/svg">
      <defs>
        <linearGradient id="workbench" x1="0" y1="0" x2="1" y2="1">
          <stop offset="0" stop-color="#b87a55"/>
          <stop offset=".35" stop-color="#3a3a3c"/>
          <stop offset=".7" stop-color="#1f2224"/>
          <stop offset="1" stop-color="#4a6e80"/>
        </linearGradient>
        <linearGradient id="strip" x1="0" y1="0" x2="1" y2="0">
          <stop offset="0" stop-color="#8a7768"/>
          <stop offset=".35" stop-color="#b9a777"/>
          <stop offset=".65" stop-color="#a58f7e"/>
          <stop offset="1" stop-color="#6f6763"/>
        </linearGradient>
      </defs>
      <path role="img" aria-label="Close-up photo of handmade rings and pendants on a dark workbench"
            d="M364,150 C270,195 160,255 110,318 C150,400 230,475 364,530 Z" fill="url(#workbench)"/>
      <path d="M285,165 C320,200 340,290 318,378 L364,385 L364,150 Z" fill="var(--teal)"/>
      <path d="M364,385 C300,410 258,470 248,520 C290,560 338,585 364,597 Z" fill="var(--teal)"/>
      <path d="M364,122 C250,190 120,262 96,317 C150,420 270,540 364,597" fill="none" stroke="var(--teal)" stroke-width="3"/>
      <g role="img" aria-label="Strip of photos: a student at the bench, finished rings, enamel pieces and a class group">
        <rect x="0" y="979" width="364" height="66" fill="url(#strip)"/>
        <path d="M96,979 L86,1045 M185,979 L175,1045 M272,979 L262,1045" stroke="var(--paper)" stroke-width="3"/>
      </g>
    </svg>

    <div class="brand">
      <div class="brand-mark"></div>
      <div class="brand-name">MARA LINDEN</div>
      <div class="brand-sub">jewellery</div>
    </div>

    <div class="headline">
      <div class="headline-lead"><span class="hl">you want to be</span> a</div>
      <div class="headline-main">jewellery</div>
      <div class="headline-accent">designer?</div>
    </div>

    <div class="offer">
      <span class="offer-line">Part time and full-time</span>
      <span class="offer-line">classes available in:</span>
    </div>

    <ul class="courses">
      <li>Silversmithing</li>
      <li>Jewellery design &amp; rendering</li>
      <li>Stone setting</li>
      <li>Gemmology</li>
      <li>Enamelling</li>
      <li>Computer aided design</li>
    </ul>

    <div class="footer-band"></div>
  </div>
  <div class="size-note">Poster size : 60cm X 180cm</div>
</div>
</body>
</html>
```